VORTELO.CH UI Contest - design ONE Tap Market screenshots for a health + fitness app

Vortelo.ch is a tech incubator on a beach in Thailand and we're looking for a superstar UX/UI designer - the winner of this contest will be invited to work with us remotely and will be considered for the full incubator program!
For this contest, you will need to design ONE highly representative screenshot of an Android app. We will take all the submitted screenshots and will then A/B test them in Brisk Shelf on a selection of audiences (US M+F 14-45) - the screenshots that have the best conversion rate wins! We then would expect the winner of the content to design the final 2 screenshots for us as part of the contest.
I'm attaching an explanation of how the app works and design considerations in a ppt. The basic idea is that we have developed a mobile app that allows you to accurately track your cardio respiratory health + fitness level, stress levels and cognitive levels from your phone; without any other devices - only using your phone camera. It allows us to see what effect the things that you do in your daily life have on your fitness, cardio, stress and cognitive levels. For example for fitness, we can detect that your fitness level has improved after even 2-3 sessions of walking; while it would take you months to see the results on your body in the gym. We can detect your stress levels increasing before you are starting to get sick and notice it yourself.
We have tested the software in a marathon style event, where we test a group's levels of fitness, stress and cognitive levels then give them recommendations and test them again after a month - whoever improved the most; gets a prize.
Right now, the software acts as a basic tracker, but we are hoping to add recommendations too and that's what will inform the final design. So you set your goals, track your levels for a few days and then we provide recommendations to you, based on other folks successful experiences and on your personal level.
We are very open minded so feel free to experiment – the ideas that we have presented in the doc are not exhaustive so if you have an idea for a better screenshot/app layout/UX/UI or even an entire new concept! – email us and we can tell you if it works with our technology.
Feel free to check out mq7ry.com for an idea of a previous sports oriented app prototype that we made before.
Good luck!
Updates
Target Market(s)
Male and Female, US + EU, 14-45 age
We are looking to target people who are suffering from stress, low energy, low fitness. People who are unhappy with the way they look and feel!
Industry/Entity Type
Health And Wellness
Colors
Designer to choose colors to be used in the design.
Requirements
Must have
- Screenshots that depict the phone at least and will work well in attracting target users to download the app - they should be easy to see on a phone screen and should be colourful and appealing - check the ppt.
Nice to have
- For multiple screenshots it would be nice to have a person in the shot to make it more relatable.
Should not have
- No super sexualised images.

```html
<!DOCTYPE html>
<html lang="en">
<head>
<meta charset="utf-8">
<title>Weekly Energy Screen</title>
<link href="https://fonts.googleapis.com/css2?family=Quicksand:wght@500;700&display=swap" rel="stylesheet">
<style>
  :root {
    --page-bg: #f3f1f8;
    --screen-top: #24107a;
    --screen-bottom: #4a0a66;
    --ink-dark: #2a0f78;
    --white: #ffffff;
    --magenta: #d60ce6;
    --blue: #2d95ff;
    --green: #5fdd2c;
    --yellow: #f2dc22;
    --orange: #ff7f2a;
    --red: #ff3b5c;
    --pink: #ff2fb0;
    --sun-bar: #cc18d8;
  }
  * { box-sizing: border-box; margin: 0; padding: 0; }
  html, body {
    width: 1200px; height: 1200px; overflow: hidden;
    background: var(--page-bg);
    font-family: "Quicksand", sans-serif;
  }
  .app-screen {
    position: absolute; left: 320px; top: 50px;
    width: 560px; height: 1100px;
    border-radius: 48px; overflow: hidden;
    background: linear-gradient(180deg, var(--screen-top) 0%, var(--screen-bottom) 60%);
    box-shadow: 0 20px 50px rgba(40, 10, 100, 0.25);
  }
  .period-tabs {
    position: absolute; top: 36px; left: 24px; right: 24px; height: 52px;
    background: var(--white); border-radius: 26px;
    display: flex; align-items: center; padding: 5px;
  }
  .period-tab {
    flex: 1; text-align: center; font-size: 20px; font-weight: 700;
    color: var(--ink-dark); line-height: 42px; border-radius: 21px;
  }
  .period-tab.is-active { background: var(--ink-dark); color: var(--white); }
  .week-range {
    position: absolute; top: 104px; width: 100%; text-align: center;
    color: var(--white); font-size: 22px; font-weight: 700; letter-spacing: 0.5px;
  }
  .energy-chart { position: absolute; top: 150px; left: 0; width: 560px; height: 470px; }
  .energy-chart text { font-family: "Quicksand", sans-serif; font-weight: 700; }
  .axis-label { fill: rgba(255,255,255,0.85); font-size: 17px; }
  .day-label { fill: var(--white); font-size: 16px; }
  .activity-card {
    position: absolute; left: 0; width: 560px; height: 140px;
    border-radius: 28px; display: flex; align-items: center;
    padding: 0 28px 0 22px; color: var(--white);
    box-shadow: 0 -6px 14px rgba(0,0,0,0.12);
  }
  .activity-card.is-sports { top: 620px; background: var(--magenta); }
  .activity-card.is-biking { top: 735px; background: var(--blue); }
  .activity-card.is-swimming { top: 850px; background: var(--green); }
  .activity-card.is-trekking { top: 965px; background: var(--yellow); }
  .activity-card.is-next { top: 1080px; background: var(--orange); }
  .activity-icon {
    flex: none; width: 92px; height: 92px; border-radius: 50%;
    background: var(--white);
    box-shadow: 0 0 0 10px rgba(255,255,255,0.35), 0 0 0 20px rgba(255,255,255,0.15);
    display: flex; align-items: center; justify-content: center;
  }
  .activity-text { flex: 1; text-align: right; }
  .activity-date { font-size: 20px; font-weight: 500; }
  .activity-title { font-size: 24px; font-weight: 700; margin-top: 4px; }
</style>
</head>
<body>
<main class="app-screen">
  <nav class="period-tabs">
    <span class="period-tab">Daily</span>
    <span class="period-tab is-active">Weekly</span>
    <span class="period-tab">Monthly</span>
  </nav>
  <p class="week-range">4-11 March 2018</p>

  <svg class="energy-chart" viewBox="0 0 560 470" aria-label="Weekly energy chart">
    <text class="axis-label" x="22" y="44">Energy</text>
    <text class="axis-label" x="30" y="86">100</text>
    <text class="axis-label" x="38" y="166">80</text>
    <text class="axis-label" x="38" y="246">60</text>
    <text class="axis-label" x="38" y="326">40</text>
    <text class="axis-label" x="38" y="406">20</text>

    <rect x="96"  y="414" width="52" height="70"  rx="8" fill="var(--sun-bar)"/>
    <rect x="158" y="142" width="52" height="342" rx="8" fill="var(--blue)"/>
    <rect x="220" y="318" width="52" height="166" rx="8" fill="var(--green)"/>
    <rect x="282" y="286" width="52" height="198" rx="8" fill="var(--yellow)"/>
    <rect x="344" y="374" width="52" height="110" rx="8" fill="var(--orange)"/>
    <rect x="406" y="158" width="52" height="326" rx="8" fill="var(--red)"/>
    <rect x="468" y="54"  width="52" height="430" rx="8" fill="var(--pink)"/>

    <text class="day-label" x="122" y="455" text-anchor="middle">Sun</text>
    <text class="day-label" x="184" y="455" text-anchor="middle">Mon</text>
    <text class="day-label" x="246" y="455" text-anchor="middle">Tue</text>
    <text class="day-label" x="308" y="455" text-anchor="middle">Wed</text>
    <text class="day-label" x="370" y="455" text-anchor="middle">Thu</text>
    <text class="day-label" x="432" y="455" text-anchor="middle">Fri</text>
    <text class="day-label" x="494" y="455" text-anchor="middle">Sat</text>
  </svg>

  <section class="activity-card is-sports">
    <div class="activity-icon">
      <svg width="48" height="48" viewBox="0 0 48 48" fill="none" stroke="var(--magenta)" stroke-width="2.5" stroke-linejoin="round" aria-label="Trophy">
        <path d="M14 8h20v10a10 10 0 0 1-20 0z"/>
        <path d="M14 12H7a7 7 0 0 0 8 10M34 12h7a7 7 0 0 1-8 10"/>
        <path d="M24 28v8M16 42h16l-2-6H18z"/>
      </svg>
    </div>
    <div class="activity-text">
      <p class="activity-date">Sunday, 4 March 2018</p>
      <p class="activity-title">Inter-church Sports Fest</p>
    </div>
  </section>

  <section class="activity-card is-biking">
    <div class="activity-icon">
      <svg width="52" height="40" viewBox="0 0 52 40" fill="none" stroke="var(--blue)" stroke-width="2.5" stroke-linejoin="round" aria-label="Bicycle">
        <circle cx="12" cy="28" r="9"/>
        <circle cx="40" cy="28" r="9"/>
        <path d="M12 28l9-14h14l5 14M21 14l7 14h12M30 8h7"/>
      </svg>
    </div>
    <div class="activity-text">
      <p class="activity-date">Monday, 5 March 2018</p>
      <p class="activity-title">Biking at The Uptown Trail</p>
    </div>
  </section>

  <section class="activity-card is-swimming">
    <div class="activity-icon">
      <div role="img" aria-label="Swimmer icon" style="width:46px;height:30px;border-radius:15px;background:var(--green);opacity:0.8"></div>
    </div>
    <div class="activity-text">
      <p class="activity-date">Tuesday, 6 March 2018</p>
      <p class="activity-title">Swimming at Bermuda Triangle</p>
    </div>
  </section>

  <section class="activity-card is-trekking">
    <div class="activity-icon">
      <div role="img" aria-label="Hiker icon" style="width:32px;height:46px;border-radius:16px;background:var(--yellow)"></div>
    </div>
    <div class="activity-text">
      <p class="activity-date">Wednesday, 7 March 2018</p>
      <p class="activity-title">Trekking at Fernwood Park</p>
    </div>
  </section>

  <section class="activity-card is-next"></section>
</main>
</body>
</html>
```